- Morvandi Customer Service Signs
- 60 year old financial services firm in Boston's financial district, stock brokers are our clients, we've young/energetic employees and it's critical they provide unbeatable customer service to the brokers, family atmosphere

```html
<!DOCTYPE html>
<html lang="en">
<head>
<meta charset="utf-8">
<title>Mediocrity Unacceptable</title>
<link rel="stylesheet" href="https://fonts.googleapis.com/css2?family=Anton&family=Roboto+Slab:wght@900&display=swap">
<style>
  :root {
    --bg-center: #c03ae0;
    --bg-mid: #8f10b8;
    --bg-edge: #62007f;
    --bubble-faint: rgba(255, 255, 255, 0.06);
    --bubble-bright: #d63cf0;
    --headline-edge: #d44a00;
    --headline-center: #ff8a00;
    --headline-shadow: rgba(90, 0, 110, 0.55);
    --subline: #ffffff;
    --quote-mark: #e646f5;
    --rule: #2c0a5a;
  }
  html, body {
    margin: 0;
    padding: 0;
    overflow: hidden;
    background: var(--bg-edge);
  }
  .sign {
    position: relative;
    width: 943px;
    height: 1200px;
    overflow: hidden;
  }
  .sign__art {
    position: absolute;
    inset: 0;
    display: block;
  }
  .headline {
    font-family: "Anton", "Impact", sans-serif;
    font-size: 205px;
  }
  .subline {
    font-family: "Roboto Slab", "Rockwell", serif;
    font-weight: 900;
    font-size: 93px;
    fill: var(--subline);
  }
  .quote-mark {
    font-family: "Roboto Slab", "Rockwell", serif;
    font-weight: 900;
    font-size: 150px;
    fill: var(--quote-mark);
  }
</style>
</head>
<body>
<main class="sign">
  <svg class="sign__art" viewBox="0 0 943 1200" width="943" height="1200" role="img" aria-label="Mediocrity unacceptable">
    <defs>
      <radialGradient id="backdrop" cx="0.42" cy="0.48" r="0.75">
        <stop offset="0" stop-color="var(--bg-center)"/>
        <stop offset="0.45" stop-color="var(--bg-mid)"/>
        <stop offset="1" stop-color="var(--bg-edge)"/>
      </radialGradient>
      <radialGradient id="glow" cx="0.5" cy="0.5" r="0.5">
        <stop offset="0" stop-color="#f4a6ff" stop-opacity="0.55"/>
        <stop offset="1" stop-color="#f4a6ff" stop-opacity="0"/>
      </radialGradient>
      <linearGradient id="headline-fill" x1="0" x2="1" y1="0" y2="0">
        <stop offset="0" stop-color="var(--headline-edge)"/>
        <stop offset="0.5" stop-color="var(--headline-center)"/>
        <stop offset="1" stop-color="var(--headline-edge)"/>
      </linearGradient>
      <filter id="lift" x="-5%" y="-10%" width="115%" height="130%">
        <feDropShadow dx="6" dy="8" stdDeviation="4" flood-color="var(--headline-shadow)"/>
      </filter>
    </defs>

    <rect class="backdrop" width="943" height="1200" fill="url(#backdrop)"/>

    <g class="bubbles">
      <circle cx="188" cy="155" r="172" fill="var(--bubble-faint)"/>
      <circle cx="950" cy="150" r="178" fill="var(--bubble-faint)"/>
      <circle cx="656" cy="184" r="60" fill="var(--bubble-faint)"/>
      <circle cx="249" cy="781" r="143" fill="var(--bubble-faint)"/>
      <circle cx="0" cy="985" r="190" fill="var(--bubble-faint)"/>
      <circle cx="815" cy="985" r="135" fill="var(--bubble-faint)"/>
      <circle cx="870" cy="523" r="317" fill="var(--bubble-bright)" opacity="0.85"/>
    </g>

    <ellipse class="text-glow" cx="430" cy="560" rx="360" ry="140" fill="url(#glow)"/>

    <text class="quote-mark" x="76" y="440">&#8220;</text>

    <text class="headline" x="87" y="551" textLength="826" lengthAdjust="spacingAndGlyphs"
          fill="url(#headline-fill)" filter="url(#lift)">Mediocrity</text>

    <text class="subline" x="79" y="663" textLength="807" lengthAdjust="spacingAndGlyphs">UNACCEPTABLE</text>

    <rect class="rule" x="78" y="691" width="812" height="10" fill="var(--rule)"/>

    <text class="quote-mark" x="812" y="836">&#8221;</text>
  </svg>
</main>
</body>
</html>
```